Brenvick Holdings LLC, new Business cards

I'm moving offices and need new cards. Plus I'm open to modifying the current design of my card. I will keep the logo but would like to explore other layouts and fonts for the design. I've included the current double sided card for reference. I Like the navy color and white. Might be open to grays or silver. Needs to be clean and elegant.

Target Market(s)

Investors, buyers & sellers of private equities and real estate.

Contact Information for Business Card

Brenvick Holdings
Dorian P.K. Halvers, Managing Principal
418 Ostrander Ave., Suite 612
Denver, CO 80319
M: 970-555-0147, O: 303-555-0192
Dorian@brenvickholdings.example
Brenvickholdings.example

Colors
0354a2
ffffff
c4c4c4

Requirements
Must have
• Business card details.
• Logo raised or embossed, it was designed after a wax seal. Current has raised ink.
Nice to have
• Space on card to write additional notes.

```html
<!DOCTYPE html>
<html lang="en">
<head>
<meta charset="utf-8">
<title>Brenvick Holdings – Business Cards</title>
<link href="https://fonts.googleapis.com/css2?family=Montserrat:wght@400;500;700&display=swap" rel="stylesheet">
<style>
  :root {
    --navy: #24214f;
    --paper: #f7f7f5;
    --stage: #e9e7e3;
    --emboss: #e2e2df;
    --rule: #3a3766;
  }
  * { margin: 0; padding: 0; box-sizing: border-box; }
  html, body { width: 1200px; height: 873px; overflow: hidden; }
  body {
    background: var(--stage);
    font-family: 'Montserrat', sans-serif;
    color: var(--navy);
    position: relative;
  }
  .card {
    position: absolute;
    left: 260px;
    width: 680px;
    height: 389px;
    background: var(--paper);
    box-shadow: 0 2px 6px rgba(0,0,0,0.12);
  }
  .card--back { top: 35px; }
  .card--front { top: 449px; }

  /* back: blind-embossed mark */
  .emboss-mark {
    position: absolute;
    left: 50%; top: 50%;
    transform: translate(-50%, -50%);
    display: flex; align-items: center; gap: 18px;
    color: var(--emboss);
    font-weight: 700;
    font-size: 30px;
    letter-spacing: 4px;
    text-transform: uppercase;
    white-space: nowrap;
  }
  .emboss-mark .dot {
    width: 46px; height: 46px; border-radius: 50%;
    background: var(--emboss);
  }

  /* front */
  .front-mark {
    position: absolute;
    right: 40px; top: 50px;
    display: flex; align-items: center; gap: 12px;
    font-weight: 700; font-size: 15px; letter-spacing: 2px;
    text-transform: uppercase; color: var(--navy);
  }
  .front-mark .dot {
    width: 34px; height: 34px; border-radius: 50%; background: var(--navy);
  }
  .identity { position: absolute; left: 44px; top: 192px; }
  .identity .name { font-weight: 700; font-size: 25px; line-height: 1.2; }
  .identity .title { font-weight: 700; font-size: 14px; margin-top: 4px; margin-left: 10px; }
  .rule {
    position: absolute; left: 52px; right: 40px; top: 262px;
    height: 1px; background: var(--rule);
  }
  .contacts {
    position: absolute; left: 54px; top: 276px;
    list-style: none; font-size: 15px; line-height: 1.55;
  }
  .contacts li { display: flex; align-items: center; gap: 10px; }
  .contacts svg { width: 13px; height: 13px; fill: var(--navy); flex: none; }
  .address {
    position: absolute; right: 40px; top: 276px;
    text-align: right; font-size: 14px; line-height: 1.6; font-style: normal;
  }
  .address .web { font-weight: 700; }
</style>
</head>
<body>
  <section class="card card--back">
    <div class="emboss-mark"><span class="dot"></span>Brenvick Holdings</div>
  </section>

  <section class="card card--front">
    <div class="front-mark"><span class="dot"></span>Brenvick Holdings</div>
    <div class="identity">
      <div class="name">Dorian P.K. Halvers</div>
      <div class="title">Managing Principal</div>
    </div>
    <div class="rule"></div>
    <ul class="contacts">
      <li><svg viewBox="0 0 16 16" aria-hidden="true"><path d="M3 1l3 3-1.5 2c1 2 3 4 5 5L11.5 9.5l3 3-2 2.5C7 15 1 9 1 3z"/></svg>303.555.0192</li>
      <li><svg viewBox="0 0 16 16" aria-hidden="true"><path d="M4 0h8v16H4zM5.5 2v10h5V2z"/></svg>970.555.0147</li>
      <li><svg viewBox="0 0 16 16" aria-hidden="true"><path d="M0 3h16v10H0zM1.5 4.5L8 9l6.5-4.5v-.2H1.5z"/></svg>dorian@brenvickholdings.example</li>
    </ul>
    <address class="address">
      418 Ostrander Ave., Suite 612<br>
      Denver, CO 80319<br>
      <span class="web">www.brenvickholdings.example</span>
    </address>
  </section>
</body>
</html>
```